Business cards for a naturopathic day clinic for stem cell therapy

We need a basic design for a day clinic, that offers stem cell therapies for Lyme therapy and other severe chronic illnesses.
Our name is "Haus solvaKrĂ¤ut", which can be translated into "Manor solvaHerb". We are a couple of naturopaths working along side physiotherapists and osteopaths, yoga teachers and massage therapists. I attached our logo.

```html
<!DOCTYPE html>
<html lang="en">
<head>
<meta charset="utf-8">
<title>Haus solvaKräut – Business Cards</title>
<link rel="stylesheet" href="https://fonts.googleapis.com/css2?family=Roboto+Slab:wght@300;400&display=swap">
<style>
  :root {
    --stage: #2e2e2e;
    --card-top: #f7f7f6;
    --card-bottom: #ecebea;
    --tint: #e6eAd6;
    --tint-soft: rgba(230, 234, 214, 0);
    --brand-green: #8db33c;
    --text-brown: #7d6f62;
    --text-grey: #6b6661;
    --rule: #a09282;
  }
  * { margin: 0; padding: 0; box-sizing: border-box; }
  html, body {
    width: 1200px; height: 900px; overflow: hidden;
    background: var(--stage);
    font-family: "Roboto Slab", Georgia, serif;
  }
  .stage {
    position: relative; width: 1200px; height: 900px;
    display: flex; flex-direction: column; align-items: center; justify-content: center;
    gap: 48px;
  }
  .card {
    position: relative; width: 640px; height: 366px; overflow: hidden;
    background: linear-gradient(160deg, var(--card-top), var(--card-bottom));
    box-shadow: 0 10px 24px rgba(0,0,0,.45);
  }
  .card-texture { position: absolute; inset: 0; }
  .card-front .card-texture {
    background: linear-gradient(90deg, var(--tint-soft) 55%, var(--tint) 100%);
  }
  .card-back .card-texture {
    background: linear-gradient(90deg, var(--tint) 0%, var(--tint-soft) 50%);
  }

  .brand {
    position: absolute; display: flex; align-items: center; gap: 14px;
    font-weight: 300; color: var(--text-brown); letter-spacing: .5px; white-space: nowrap;
  }
  .brand-dot { width: 30px; height: 30px; border-radius: 50%; background: var(--brand-green); flex: none; }
  .card-front .brand { left: 70px; top: 150px; font-size: 40px; }

  .holder { position: absolute; left: 44px; top: 146px; }
  .holder-name { font-size: 24px; font-weight: 300; color: var(--brand-green); }
  .holder-role { font-size: 15px; font-weight: 300; color: var(--text-grey); margin-top: 2px; }

  .contact-list {
    position: absolute; left: 352px; top: 58px; list-style: none;
    font-size: 14px; font-weight: 300; color: var(--text-grey); line-height: 1.25;
  }
  .contact-list li { display: flex; align-items: flex-start; gap: 9px; margin-bottom: 9px; }
  .contact-list svg { width: 13px; height: 13px; flex: none; margin-top: 3px; fill: var(--text-brown); }
  .contact-rule { position: absolute; left: 340px; right: 0; top: 218px; height: 1.5px; background: var(--rule); }
  .card-back .brand { left: 340px; top: 246px; font-size: 32px; gap: 12px; }
  .card-back .brand-dot { width: 24px; height: 24px; }
</style>
</head>
<body>
<main class="stage">

  <section class="card card-front" aria-label="Card front">
    <div class="card-texture" role="img" aria-label="Soft pale green background decoration"></div>
    <div class="brand"><span class="brand-dot"></span>Haus solvaKräut</div>
  </section>

  <section class="card card-back" aria-label="Card back">
    <div class="card-texture" role="img" aria-label="Soft pale green background decoration"></div>

    <div class="holder">
      <p class="holder-name">Lena Marsh</p>
      <p class="holder-role">Director</p>
    </div>

    <ul class="contact-list">
      <li><svg viewBox="0 0 16 16"><path d="M3 2h3l1 4-2 1c1 2 2 3 4 4l1-2 4 1v3c0 1-1 1-2 1C6 14 2 10 2 4c0-1 0-2 1-2z"/></svg>0412558017</li>
      <li><svg viewBox="0 0 16 16"><path d="M1 3h14v10H1z M2 4l6 5 6-5" fill="none" stroke="var(--text-brown)" stroke-width="1.6"/></svg>lena@haussolvakraeut.com.au</li>
      <li><svg viewBox="0 0 16 16"><circle cx="8" cy="8" r="6.5" fill="none" stroke="var(--text-brown)" stroke-width="1.5"/><path d="M1.5 8h13M8 1.5c-3 3-3 10 0 13M8 1.5c3 3 3 10 0 13" fill="none" stroke="var(--text-brown)" stroke-width="1.2"/></svg>www.haussolvakraeut.com.au</li>
      <li><svg viewBox="0 0 16 16"><path d="M8 1a5 5 0 0 1 5 5c0 4-5 9-5 9S3 10 3 6a5 5 0 0 1 5-5zm0 3a2 2 0 1 0 0 4 2 2 0 0 0 0-4z"/></svg><span>P.O Box 0000 dummy<br>Dummy Land Dummy, 0000</span></li>
    </ul>
    <div class="contact-rule"></div>

    <div class="brand"><span class="brand-dot"></span>Haus solvaKräut</div>
  </section>

</main>
</body>
</html>
```